Updated Stationary needed using new logo for Hair Tissue Mineral Analysis Company

Simple stationary design needed using new logo!
1. 8.5" x 11" Letterhead with company information listed below
2. 8.5" x 11" Design with Footer only with logo and information for print materials
3. 5.5" x 8.5" letterhead design
4. 4.125" x 9.5" Business envelope (#10 envelope) with address
5. 4.125" x 9.5" Business envelope with clear window (#10 envelope) with address
6. 6.5" x 9.5" envelope (6 3/4 Booklet envelope) with address
7. 10" x 13" Open End envelope
Address:
4817 N. Corwin Street
Corvale, AZ 85390
Phone:
(602)-417-3926
Website:
www.pexumor.com
Email:
information@pexumor.com
Updates
Need extra days to review
Focused on completing other projects first
Look and feel
Each slider illustrates characteristics of the customer's brand and the style your logo design should communicate.

```html
<!DOCTYPE html>
<html lang="en">
<head>
<meta charset="utf-8">
<title>Pexumor Labs Stationery Set</title>
<link href="https://fonts.googleapis.com/css2?family=Montserrat:wght@400;600;700&family=Open+Sans:wght@400&display=swap" rel="stylesheet">
<style>
  :root{
    --backdrop:#c8c8c8;
    --paper:#ffffff;
    --orange:#f58220;
    --blue:#2e59a3;
    --ink:#3a3a3a;
    --muted:#555555;
    --window:#a9a9a9;
  }
  *{box-sizing:border-box;margin:0;padding:0}
  html,body{width:1200px;height:645px;overflow:hidden}
  body{background:var(--backdrop);position:relative;font-family:"Open Sans",sans-serif;color:var(--ink)}
  .sheet{position:absolute;background:var(--paper);box-shadow:0 1px 3px rgba(0,0,0,.25);overflow:hidden}
  .footer-swoosh{position:absolute;left:0;bottom:0;width:100%}
  .flap{position:absolute;left:0;top:0;width:100%}
  .flap-brand{position:absolute;left:0;width:100%;text-align:center;font-family:"Montserrat",sans-serif;font-weight:700;color:var(--paper);letter-spacing:.04em}
  .brand{position:absolute;font-family:"Montserrat",sans-serif;font-weight:700;color:var(--blue);white-space:nowrap;letter-spacing:.03em}
  .contact{position:absolute;font-family:"Montserrat",sans-serif;color:var(--ink);border-left:.6px solid var(--orange);line-height:1.35;white-space:nowrap}
  .contact .gap{height:.5em}
  .contact .ico{display:inline-block;width:.75em;height:.75em;background:var(--orange);border-radius:50%;margin-right:.35em;vertical-align:-.05em}
  .recipient{position:absolute;line-height:1.5}
  .recipient .name{font-size:1.35em;text-transform:uppercase}
  .letter-body{position:absolute;text-align:justify;line-height:1.7;color:var(--muted)}
  .letter-body p{margin-bottom:1.4em}
  .closing{position:absolute;color:var(--muted)}
  .closing .signer{margin-top:2.2em;font-size:1.45em;color:var(--ink)}
  .return-address{position:absolute;font-family:"Montserrat",sans-serif;line-height:1.4;color:var(--ink);white-space:nowrap}
  .address-window{position:absolute;background:var(--window);border-radius:8px}
</style>
</head>
<body>

<!-- Full letterhead -->
<section class="sheet letterhead" style="left:85px;top:30px;width:218px;height:281px;">
  <div class="brand" style="left:23px;top:21px;font-size:9px;">PEXUMOR LABS</div>
  <div class="contact" style="left:141px;top:13px;font-size:4px;padding-left:4px;">
    4817 N. Corwin Street<br>Corvale, AZ 85390
    <div class="gap"></div>
    <span class="ico"></span>(602)-417-3926<br>
    <span class="ico"></span>information@pexumor.com<br>
    <span class="ico"></span>www.pexumor.com
  </div>
  <div class="recipient" style="left:23px;top:66px;font-size:2.9px;">
    <div class="name">Dana Whitfield</div>
    Chief Executive Officer<br>City/State, Zip Code
  </div>
  <div class="letter-body" style="left:23px;top:103px;width:172px;font-size:3px;">
    <p>Thank you for choosing our laboratory for your hair tissue mineral analysis. Your results are enclosed with a clear summary of each element we measured, along with short notes on what the values may mean for your ongoing wellness plan. We suggest you review the full report with your practitioner, who can compare these readings with your history, diet and any supplements you take, and then decide on the next steps that suit you best.</p>
    <p>Every sample is prepared under strict lab protocols and checked twice before results are released. If any reading falls outside the expected range, our team adds a brief comment so the result is easy to follow. We also include a simple chart that shows how each mineral compares with typical levels, making it easier to spot patterns and track changes over time when you send a new sample in the months ahead.</p>
    <p>Should you have any questions about this report, please contact our office by phone or email and a member of our staff will reply within two business days. We value your trust and look forward to supporting your health goals with accurate, timely and easy to read laboratory results for many years to come.</p>
  </div>
  <div class="closing" style="left:23px;top:219px;font-size:2.9px;">Sincerely,<div class="signer">Owen Carver</div></div>
  <svg class="footer-swoosh" height="15" viewBox="0 0 200 20" preserveAspectRatio="none" aria-hidden="true">
    <path d="M0 20 Q70 3 150 1 L150 2 Q80 6 20 20 Z" fill="var(--orange)"/>
    <path d="M40 20 Q110 6 200 4 L200 20 Z" fill="var(--blue)"/>
  </svg>
</section>

<!-- Footer-only sheet -->
<section class="sheet footer-sheet" style="left:342px;top:30px;width:218px;height:281px;">
  <div class="brand" style="left:23px;top:244px;font-size:9px;">PEXUMOR LABS</div>
  <div class="contact" style="left:141px;top:235px;font-size:4px;padding-left:4px;">
    4817 N. Corwin Street<br>Corvale, AZ 85390
    <div class="gap"></div>
    <span class="ico"></span>(602)-417-3926<br>
    <span class="ico"></span>information@pexumor.com<br>
    <span class="ico"></span>www.pexumor.com
  </div>
  <svg class="footer-swoosh" height="15" viewBox="0 0 200 20" preserveAspectRatio="none" aria-hidden="true">
    <path d="M0 20 Q70 3 150 1 L150 2 Q80 6 20 20 Z" fill="var(--orange)"/>
    <path d="M40 20 Q110 6 200 4 L200 20 Z" fill="var(--blue)"/>
  </svg>
</section>

<!-- Half letterhead -->
<section class="sheet letterhead-half" style="left:597px;top:29px;width:183px;height:283px;">
  <div class="brand" style="left:13px;top:24px;font-size:7.5px;">PEXUMOR LABS</div>
  <div class="contact" style="left:110px;top:13px;font-size:4px;padding-left:4px;">
    4817 N. Corwin Street<br>Corvale, AZ 85390
    <div class="gap"></div>
    <span class="ico"></span>(602)-417-3926<br>
    <span class="ico"></span>information@pexumor.com<br>
    <span class="ico"></span>www.pexumor.com
  </div>
  <div class="recipient" style="left:13px;top:62px;font-size:2.6px;">
    <div class="name">Dana Whitfield</div>
    Chief Executive Officer<br>City/State, Zip Code
  </div>
  <div class="letter-body" style="left:13px;top:98px;width:157px;font-size:2.6px;">
    <p>Thank you for choosing our laboratory for your hair tissue mineral analysis. Your results are enclosed with a clear summary of each element we measured, along with short notes on what the values may mean for your ongoing wellness plan. We suggest you review the full report with your practitioner, who can compare these readings with your history, diet and any supplements you take, and then decide on the next steps that suit you best.</p>
    <p>Every sample is prepared under strict lab protocols and checked twice before results are released. If any reading falls outside the expected range, our team adds a brief comment so the result is easy to follow. We also include a simple chart that shows how each mineral compares with typical levels, making it easier to spot patterns and track changes over time when you send a new sample in the months ahead.</p>
    <p>Should you have any questions about this report, please contact our office by phone or email and a member of our staff will reply within two business days. We value your trust and look forward to supporting your health goals with accurate, timely and easy to read laboratory results for many years to come.</p>
  </div>
  <div class="closing" style="left:13px;top:202px;font-size:2.6px;">Sincerely,<div class="signer">Owen Carver</div></div>
  <svg class="footer-swoosh" height="12" viewBox="0 0 200 20" preserveAspectRatio="none" aria-hidden="true">
    <path d="M0 20 Q70 3 150 1 L150 2 Q80 6 20 20 Z" fill="var(--orange)"/>
    <path d="M40 20 Q110 6 200 4 L200 20 Z" fill="var(--blue)"/>
  </svg>
</section>

<!-- #10 envelope back -->
<section class="sheet envelope-back" style="left:818px;top:29px;width:296px;height:130px;">
  <svg class="flap" height="46" viewBox="0 0 300 50" preserveAspectRatio="none" aria-hidden="true">
    <path d="M0 0 H300 L290 36 Q286 50 272 50 H28 Q14 50 10 36 Z" fill="var(--orange)"/>
  </svg>
  <div class="flap-brand" style="top:6px;font-size:26px;">PEXUMOR</div>
</section>

<!-- #10 envelope front -->
<section class="sheet envelope-front" style="left:818px;top:187px;width:296px;height:129px;">
  <div class="brand" style="left:14px;top:14px;font-size:8.5px;">PEXUMOR LABS</div>
  <div class="return-address" style="left:14px;top:33px;font-size:5px;">4817 N. Corwin Street<br>Corvale, AZ 85390</div>
  <svg class="footer-swoosh" height="20" viewBox="0 0 200 20" preserveAspectRatio="none" aria-hidden="true">
    <path d="M0 20 Q70 3 150 1 L150 2 Q80 6 20 20 Z" fill="var(--orange)"/>
    <path d="M40 20 Q110 6 200 4 L200 20 Z" fill="var(--blue)"/>
  </svg>
</section>

<!-- Window envelope back -->
<section class="sheet envelope-back" style="left:85px;top:337px;width:299px;height:129px;">
  <svg class="flap" height="48" viewBox="0 0 300 50" preserveAspectRatio="none" aria-hidden="true">
    <path d="M0 0 H300 L290 36 Q286 50 272 50 H28 Q14 50 10 36 Z" fill="var(--orange)"/>
  </svg>
  <div class="flap-brand" style="top:6px;font-size:28px;">PEXUMOR</div>
</section>

<!-- Booklet envelope back -->
<section class="sheet envelope-back" style="left:419px;top:337px;width:190px;height:130px;">
  <svg class="flap" height="30" viewBox="0 0 300 50" preserveAspectRatio="none" aria-hidden="true">
    <path d="M0 0 H300 L290 36 Q286 50 272 50 H28 Q14 50 10 36 Z" fill="var(--orange)"/>
  </svg>
  <div class="flap-brand" style="top:4px;font-size:16px;">PEXUMOR</div>
</section>

<!-- Small letterhead -->
<section class="sheet letterhead-small" style="left:668px;top:354px;width:183px;height:237px;">
  <div class="brand" style="left:9px;top:10px;font-size:6.5px;">PEXUMOR LABS</div>
  <div class="return-address" style="left:9px;top:23px;font-size:2.6px;">4817 N. Corwin Street<br>Corvale, AZ 85390</div>
  <svg class="footer-swoosh" height="11" viewBox="0 0 200 20" preserveAspectRatio="none" aria-hidden="true">
    <path d="M0 20 Q70 3 150 1 L150 2 Q80 6 20 20 Z" fill="var(--orange)"/>
    <path d="M40 20 Q110 6 200 4 L200 20 Z" fill="var(--blue)"/>
  </svg>
</section>

<!-- Open end envelope -->
<section class="sheet envelope-open-end" style="left:880px;top:352px;width:185px;height:240px;">
  <svg class="flap" height="29" viewBox="0 0 300 50" preserveAspectRatio="none" aria-hidden="true">
    <path d="M0 0 H300 L290 36 Q286 50 272 50 H28 Q14 50 10 36 Z" fill="var(--orange)"/>
  </svg>
  <div class="flap-brand" style="top:5px;font-size:15px;">PEXUMOR</div>
</section>

<!-- Window envelope front -->
<section class="sheet envelope-window" style="left:85px;top:486px;width:299px;height:129px;">
  <div class="brand" style="left:14px;top:14px;font-size:8.5px;">PEXUMOR LABS</div>
  <div class="return-address" style="left:14px;top:33px;font-size:5px;">4817 N. Corwin Street<br>Corvale, AZ 85390</div>
  <div class="address-window" style="left:15px;top:74px;width:142px;height:35px;"></div>
  <svg class="footer-swoosh" height="20" viewBox="0 0 200 20" preserveAspectRatio="none" aria-hidden="true">
    <path d="M0 20 Q70 3 150 1 L150 2 Q80 6 20 20 Z" fill="var(--orange)"/>
    <path d="M40 20 Q110 6 200 4 L200 20 Z" fill="var(--blue)"/>
  </svg>
</section>

<!-- Booklet envelope front -->
<section class="sheet envelope-booklet" style="left:419px;top:485px;width:190px;height:130px;">
  <div class="brand" style="left:11px;top:11px;font-size:7px;">PEXUMOR LABS</div>
  <div class="return-address" style="left:11px;top:27px;font-size:3px;">4817 N. Corwin Street<br>Corvale, AZ 85390</div>
  <svg class="footer-swoosh" height="15" viewBox="0 0 200 20" preserveAspectRatio="none" aria-hidden="true">
    <path d="M0 20 Q70 3 150 1 L150 2 Q80 6 20 20 Z" fill="var(--orange)"/>
    <path d="M40 20 Q110 6 200 4 L200 20 Z" fill="var(--blue)"/>
  </svg>
</section>

</body>
</html>
```